UK based media owner TALVEX (http://www.talvex.uk/) needs DIGITAL ADVERT to run on our digital panel

Hi guys,

Thanks for taking the time to have a look at this brief.
I need someone to create a digital advert (still/static design or video) to run on our digital panels which are located across UK university student unions.
For who wants to upload a video ---> All of our panels are digitally enabled and allow for full motion video – they run adverts 10 seconds long (see artwork specification document in attachment) therefore the advert will have to be 10 seconds long.
For static/still design ----> see artwork specification to see resolution etc

I need something professional looking, polished yet fresh and exciting so that it speaks and connects to this younger audience – we want to inspire them to take a step towards new levels of business opportunities.

Here are some Key Points you’ll need to take into consideration when designing the advert:

Overall Campaign Objective: To excite and attract young entrepreneurs to get in touch with us for possible partnerships

Target Audience: Young entrepreneurs attending university (university students – 18 to 24 years old)

Creative Specifications: See attached document with artwork specifications

Text on Advert:

I need the following text to appear on the advert: (Please include company logo)

“Do you have a business idea that would benefit with advertising on these screens?

We want to support young entrepreneurs and will partner with any whom have a great idea

WE WANT TO HEAR FROM YOU!

Email us at ideas@talvex.uk
www.talvex.uk/ideas”

I would need some ideas by the 3rd July 2018 if possible.

Thanks to all who will take part in this project – contact me if you have any questions

Target Market(s)

Young entrepreneurs attending university (university students – 18 to 24 years old)

Requirements
Must have
• I need the following text to appear on the advert: (Please include company logo)
• “Do you have a business idea that would benefit with advertising on these screens?
• We want to support young entrepreneurs and will partner with any whom have a great idea
• WE WANT TO HEAR FROM YOU!
• Email us at ideas@talvex.uk
• www.talvex.uk/ideas”

```html
<!DOCTYPE html>
<html lang="en">
<head>
<meta charset="utf-8">
<title>TALVEX – Young Entrepreneurs</title>
<link href="https://fonts.googleapis.com/css2?family=Exo+2:wght@300;400;700&display=swap" rel="stylesheet">
<style>
  :root {
    --red: #d4262a;
    --red-deep: #c21f22;
    --red-light: #e0312c;
    --ink: #0c0a0a;
    --white: #ffffff;
    --hand-dark: #1c1717;
    --hand-mid: #2b1a1a;
  }
  * { margin: 0; padding: 0; box-sizing: border-box; }
  html, body { width: 675px; height: 1200px; overflow: hidden; background: var(--ink); }
  .advert {
    position: relative;
    width: 675px;
    height: 1200px;
    overflow: hidden;
    font-family: "Exo 2", "Helvetica Neue", Arial, sans-serif;
    background: radial-gradient(circle at 55% 48%, var(--red-light) 0%, var(--red) 45%, var(--red-deep) 100%);
    color: var(--white);
  }
  .hero-illustration {
    position: absolute;
    left: 280px;
    top: 0;
    width: 372px;
    height: 360px;
    border-radius: 0 0 48px 120px;
    background: linear-gradient(200deg, var(--hand-dark) 0%, var(--hand-mid) 60%, var(--red-deep) 100%);
  }
  .headline {
    position: absolute;
    left: 65px;
    top: 312px;
    font-weight: 400;
    font-size: 46px;
    line-height: 62px;
    letter-spacing: 0.3px;
  }
  .support-copy {
    position: absolute;
    left: 66px;
    top: 651px;
    font-weight: 400;
    font-size: 29px;
    line-height: 40px;
    color: var(--ink);
  }
  .call-to-action {
    position: absolute;
    left: 65px;
    top: 854px;
    width: 508px;
    height: 76px;
  }
  .call-to-action svg { position: absolute; inset: 0; }
  .call-to-action span {
    position: absolute;
    left: 22px;
    top: 0;
    line-height: 76px;
    font-weight: 700;
    font-size: 27px;
    letter-spacing: 0.2px;
    color: var(--white);
  }
  .contact {
    position: absolute;
    left: 66px;
    top: 958px;
    font-size: 25px;
    line-height: 34px;
    color: var(--ink);
  }
  .contact strong { font-weight: 700; }
  .footer-shape { position: absolute; left: 0; top: 1036px; }
  .brand-plate {
    position: absolute;
    left: 60px;
    top: 1059px;
    width: 365px;
    height: 92px;
    background: var(--red);
    display: flex;
    align-items: center;
    justify-content: center;
  }
  .brand-name {
    font-weight: 400;
    font-size: 42px;
    letter-spacing: 14px;
    padding-left: 14px;
    color: var(--white);
  }
</style>
</head>
<body>
<main class="advert">
  <div class="hero-illustration" role="img" aria-label="Illustration of a black hand reaching down and holding a red light bulb"></div>

  <h1 class="headline">Do you have<br>a Business Idea<br>that would benefit<br>with advertising on<br>these screens?</h1>

  <p class="support-copy">We want to support<br>Young Entrepreneurs<br>and will partner with any<br>whom have a great idea</p>

  <div class="call-to-action">
    <svg width="508" height="76" viewBox="0 0 508 76">
      <polygon points="1,1 474,1 507,24 507,75 1,75" fill="none" stroke="var(--white)" stroke-width="2"/>
    </svg>
    <span>WE WANT TO HEAR FROM YOU!</span>
  </div>

  <p class="contact">email us at <strong>ideas@talvex.uk</strong><br><strong>www.talvex.uk/ideas</strong></p>

  <svg class="footer-shape" width="675" height="164" viewBox="0 0 675 164">
    <polygon points="675,0 675,164 0,164 0,68 590,68" fill="var(--ink)"/>
  </svg>

  <div class="brand-plate">
    <span class="brand-name">TALVEX</span>
  </div>
</main>
</body>
</html>
```